Consulting, Investors, Joint Venture Website

Founded in April 2018, Marendo Advisers Limited (MAL) is an advisory consulting firm specializing in engaging investors in business ventures in Tanzania.
With extensive experience in construction, energy, oil and gas and the legal professions, our team assembles our expertise that allows foreign investors to set foot and flourish in the Tanzanian market.
MAL is locally owned, founded and registered. Our shareholders are cultured Tanzanian citizens with extensive corporate experience in South Africa, Tanzania, United Kingdom and the United States.

Our mission is to provide responsive and unrivalled professional advice from learned and experienced professionals versed in the local market, with an understanding of the cultural and logistical challenges faced by foreign investors.

Our vision is to provide a complete investor’s package that initiates with company registration, compliance and documentation services and ultimately operational facilitation services.

Target Market(s)

Foreign Investors, International companies

Industry/Entity Type

Business Consultant

Number of Pages Required

5+ page

Requirements
Must have
• It will be 5 pages - Home, About Us, Services, Portfolio, Contact Us
Nice to have
• if it can look like https://www.vq-sample.com/
• or https://www.torvell.com or http://www.bramwickpoint.com/

```html
<!DOCTYPE html>
<html lang="en">
<head>
<meta charset="utf-8">
<title>Marendo Advisers Limited</title>
<link href="https://fonts.googleapis.com/css2?family=Michroma&family=Lato:wght@400;700&display=swap" rel="stylesheet">
<style>
:root{
  --blue:#1e5bb0;
  --blue-dark:#174a94;
  --ink:#333a44;
  --muted:#6b7280;
  --white:#ffffff;
  --grey-bg:#f0f0f0;
  --field:#eeeeee;
  --footer:#2b2b2b;
}
*{box-sizing:border-box;margin:0;padding:0}
html,body{width:1200px;height:3571px;overflow:hidden}
body{position:relative;font-family:'Lato',sans-serif;color:var(--ink);background:var(--white)}
.display{font-family:'Michroma',sans-serif;text-transform:uppercase}
section,header,footer{position:absolute;left:0;width:1200px}
.abs{position:absolute}

/* header + hero */
.hero{top:0;height:564px}
.nav{top:0;left:0;width:1200px;height:76px;background:rgba(20,30,45,.55);z-index:2}
.brand{left:143px;top:14px;display:flex;align-items:center;gap:12px}
.brand-mark{width:44px;height:44px;border-radius:50%;background:var(--blue)}
.brand-name{font-family:'Michroma',sans-serif;font-size:22px;color:var(--white);letter-spacing:2px}
.menu{left:496px;top:24px;display:flex;gap:6px;list-style:none}
.menu li{font-family:'Michroma',sans-serif;font-size:11.5px;color:var(--white);padding:7px 14px;border-radius:16px;white-space:nowrap;text-transform:uppercase}
.menu li.active{background:var(--blue)}
.hero-circle{left:124px;top:84px;width:404px;height:404px;border-radius:50%;background:rgba(30,91,176,.72);display:flex;align-items:center;justify-content:center;text-align:center}
.hero-circle p{font-family:'Michroma',sans-serif;font-size:17px;line-height:35px;color:var(--white);text-transform:uppercase;width:350px;letter-spacing:.5px}
.dots{left:294px;top:443px;display:flex;gap:8px}
.dots span{width:10px;height:10px;border-radius:50%;background:rgba(255,255,255,.6)}
.dots span.on{background:var(--white)}

/* about */
.about{top:564px;height:412px}
.section-title{left:0;text-align:center;font-family:'Michroma',sans-serif;text-transform:uppercase;font-size:32px;color:var(--blue);width:100%;white-space:nowrap}
.about .section-title{top:66px}
.about .tag{left:0;top:108px;width:100%;text-align:center;font-family:'Michroma',sans-serif;font-size:10px;letter-spacing:6px;color:var(--muted);padding-left:140px}
.about-text{left:155px;top:142px;width:893px;text-align:center;font-size:13px;line-height:21px;color:var(--ink)}
.pillar{top:234px;display:flex;gap:14px}
.pillar .icon{width:78px;height:78px;border-radius:50%;border:2px solid var(--blue);display:flex;align-items:center;justify-content:center;flex:none}
.pillar h3{font-family:'Michroma',sans-serif;font-size:16px;color:var(--blue);margin-bottom:6px}
.pillar p{font-size:12.5px;line-height:19px;color:var(--ink);width:370px}
.mission{left:160px}
.vision{left:643px}

/* services */
.services{top:976px;height:738px;background:var(--blue)}
.services .section-title{top:88px;color:var(--white)}
.sub{left:0;width:100%;text-align:center;font-size:12.5px}
.services .sub{top:144px;color:#dfe8f5}
.grid{left:140px;top:212px;display:grid;grid-template-columns:repeat(4,230px);grid-template-rows:repeat(2,232px)}
.service{border:1px solid rgba(255,255,255,.25);padding:28px 14px 0;color:var(--white)}
.service h3{font-family:'Michroma',sans-serif;font-size:12px;margin-bottom:24px;text-transform:uppercase;white-space:nowrap}
.service p{font-size:11.5px;line-height:17px;color:#dce6f4}
.service a{display:inline-block;margin-top:10px;font-size:12px;color:#cfdcf0;text-decoration:underline}

/* cta */
.cta{top:1714px;height:257px}
.cta p{left:0;top:84px;width:100%;text-align:center;font-family:'Michroma',sans-serif;font-size:15px;line-height:26px;color:var(--ink);text-transform:uppercase}
.btn{display:inline-block;background:var(--blue);color:var(--white);font-family:'Michroma',sans-serif;font-size:13px;border-radius:20px;text-align:center;text-transform:uppercase}
.cta .btn{left:507px;top:162px;width:183px;height:36px;line-height:36px}

/* portfolio */
.portfolio{top:1971px;height:815px;background:var(--grey-bg)}
.portfolio .section-title{top:88px}
.portfolio .sub{top:144px;color:var(--ink)}
.work{display:flex;align-items:flex-end;justify-content:center;padding:0 8px 12px;text-align:center}
.work span{font-family:'Michroma',sans-serif;font-size:10.5px;color:var(--white);text-transform:uppercase;white-space:nowrap}
.work-feature{flex-direction:column;align-items:center;justify-content:center;border:3px solid rgba(255,255,255,.6);padding:0 30px}
.work-feature h3{font-family:'Michroma',sans-serif;font-size:15px;line-height:28px;color:var(--white);text-transform:uppercase;margin-bottom:22px}
.work-feature p{font-size:12.5px;line-height:19px;color:var(--white)}

/* consultation */
.consult{top:2786px;height:531px}
.consult h2{left:140px;top:86px;font-family:'Michroma',sans-serif;font-size:21px;color:var(--blue);text-transform:uppercase;white-space:nowrap}
.consult .lead{left:140px;top:136px;width:540px;font-size:12.5px;line-height:20px}
.field{background:var(--field);font-size:12px;color:#555;padding:12px 10px}
.consult .btn{left:140px;top:412px;width:184px;height:36px;line-height:36px}
.consult-photo{left:714px;top:0;width:486px;height:531px;background:linear-gradient(135deg,#2f4a6d 0%,#6f8aa8 40%,#c9d4e0 70%,#e8edf2 100%)}

/* contact band */
.contact{top:3317px;height:171px;background:var(--blue)}
.contact-col{top:0;height:171px;display:flex;flex-direction:column;align-items:center;padding-top:46px;color:var(--white);font-size:13.5px}
.contact-col .icon{width:46px;height:46px;border-radius:50%;border:2px solid var(--white);display:flex;align-items:center;justify-content:center;margin-bottom:22px}
.divider{top:45px;width:1px;height:90px;background:rgba(255,255,255,.3)}

/* footer */
.footer{top:3488px;height:83px;background:var(--footer)}
.foot-links{left:140px;top:18px;display:flex;gap:12px;list-style:none;font-size:12px;color:#ddd}
.foot-links li+li::before{content:"|";margin-right:12px;color:#777}
.copy{left:140px;top:46px;font-size:12px;color:#bbb}
.foot-brand{left:650px;top:28px;font-family:'Michroma',sans-serif;font-size:20px;color:var(--white);letter-spacing:3px}
.social{left:917px;top:24px;display:flex;gap:10px}
.social span{width:30px;height:30px;border-radius:50%;border:2px solid #ccc}
</style>
</head>
<body>

<header class="hero">
  <div class="abs" role="img" aria-label="Photograph of a hand placing a jigsaw puzzle piece" style="inset:0;background:linear-gradient(120deg,#8aa0b8,#b7c6d4 45%,#5b7390 80%,#34506e)"></div>
  <nav class="nav abs">
    <div class="brand abs"><span class="brand-mark"></span><span class="brand-name">MARENDO</span></div>
    <ul class="menu abs">
      <li class="active">Home</li><li>About Us</li><li>Services</li><li>Portfolio</li><li>Contact Us</li>
    </ul>
  </nav>
  <div class="hero-circle abs"><p>We are a advisory consulting firm specializing in engaging investors in business ventures in Tanzania.</p></div>
  <div class="dots abs"><span class="on"></span><span></span><span></span><span></span></div>
</header>

<section class="about">
  <h2 class="section-title abs">About Marendo</h2>
  <div class="tag abs">ADVISERS</div>
  <p class="about-text abs">Having extensive experience in construction, energy, oil and gas and the legal professions, our team assembles our expertise that allows foreign investors to set foot and flourish in the Tanzanian market. Our firm is locally owned, founded and registered. Our shareholders are cultured Tanzanian citizens with extensive corporate experience in South Africa, Tanzania, United Kingdom and the United States.</p>
  <div class="pillar mission abs">
    <div class="icon"><svg width="40" height="40" viewBox="0 0 40 40" fill="none" stroke="#1e5bb0" stroke-width="2"><circle cx="20" cy="20" r="15"/><circle cx="20" cy="20" r="9"/><circle cx="20" cy="20" r="3" fill="#1e5bb0"/><path d="M20 20 L36 4"/></svg></div>
    <div><h3 class="display">Our Mission</h3><p>Is to provide responsive and unrivalled professional advice from learned and experienced professionals versed in the local market, with an understanding of the cultural and logistical challenges faced by foreign investors.</p></div>
  </div>
  <div class="pillar vision abs">
    <div class="icon"><svg width="42" height="30" viewBox="0 0 42 30" fill="none" stroke="#1e5bb0" stroke-width="2"><path d="M2 15 Q21 -5 40 15 Q21 35 2 15Z"/><circle cx="21" cy="15" r="6" fill="#1e5bb0"/></svg></div>
    <div><h3 class="display">Our Vision</h3><p>Is to provide a complete investor's package that initiates with company registration, compliance and documentation services and ultimately operational facilitation services.</p></div>
  </div>
</section>

<section class="services">
  <h2 class="section-title abs">Our Services</h2>
  <p class="sub abs">Lorem ipsum dolor sit amet, consectetuer adipiscing elit, sed diam nonummy nibh euismod tincidunt ut laoreet dolore magna aliquam erat volutpat.</p>
  <div class="grid abs">
    <div role="img" aria-label="Photograph of engineers in hard hats at a construction site" style="background:linear-gradient(160deg,#4d7fc0,#a7c2de 50%,#c9b35a)"></div>
    <div class="service"><h3>Energy</h3><p>Lorem ipsum dolor sit amet consetuer adipiscing elit, sed diam nonummy nibh euismod tincidunt ut laoreet dolore the ipsum dolor sit amet consetuer.</p><a>Read More »</a></div>
    <div role="img" aria-label="Photograph of an offshore oil platform at sea" style="background:linear-gradient(180deg,#1d4f8f,#3d78b8 55%,#103868)"></div>
    <div class="service"><h3>Legal Professions</h3><p>Lorem ipsum dolor sit amet consetuer adipiscing elit, sed diam nonummy nibh euismod tincidunt ut laoreet dolore the ipsum dolor sit amet consetuer.</p><a>Read More »</a></div>
    <div class="service"><h3>Construction</h3><p>Lorem ipsum dolor sit amet consetuer adipiscing elit, sed diam nonummy nibh euismod tincidunt ut laoreet dolore the ipsum dolor sit amet consetuer.</p><a>Read More »</a></div>
    <div role="img" aria-label="Illustration of a hand holding wind turbines and solar panels on grass" style="background:linear-gradient(180deg,#8ec3ec,#d8ecf8 45%,#7fb34a 80%,#e6cdb5)"></div>
    <div class="service"><h3>Oil and Gas</h3><p>Lorem ipsum dolor sit amet consetuer adipiscing elit, sed diam nonummy nibh euismod tincidunt ut laoreet dolore the ipsum dolor sit amet consetuer.</p><a>Read More »</a></div>
    <div role="img" aria-label="Photograph of a business handshake over documents" style="background:linear-gradient(135deg,#e9e9ea,#9a9ca0 50%,#2a2c31)"></div>
  </div>
</section>

<section class="cta">
  <p class="abs">Lorem ipsum dolor sit amet, consectetuer adipiscing elit, sed diam<br>nonummy nibh euismod tincidunt ut laoreet.</p>
  <span class="btn abs">Get Started</span>
</section>

<section class="portfolio">
  <h2 class="section-title abs">Our Portfolio</h2>
  <p class="sub abs">Lorem ipsum dolor sit amet, consectetuer adipiscing elit, sed diam nonummy nibh euismod tincidunt ut laoreet dolore magna aliquam erat volutpat.</p>
  <div class="work abs" role="img" aria-label="Photograph of a business meeting around a table" style="left:140px;top:215px;width:291px;height:250px;background:linear-gradient(160deg,#5c6e5a,#8e9a88 50%,#2f3a33)"><span>Lorem ipsum dolor sit amet</span></div>
  <div class="work abs" role="img" aria-label="Photograph of a businesswoman writing on documents" style="left:140px;top:484px;width:291px;height:245px;background:linear-gradient(150deg,#f2f2f4,#c7c9d2 50%,#8a8fa0)"><span>Lorem ipsum dolor sit amet</span></div>
  <div class="work work-feature abs" role="img" aria-label="Photograph of wind turbines at sunset" style="left:457px;top:215px;width:288px;height:514px;background:linear-gradient(180deg,#2c4666,#4b6587 45%,#3b4a57 75%,#121820)">
    <h3>Lorem ipsum dolor<br>sit amet</h3>
    <p>Lorem ipsum dolor sit amet, consectetuer adipiscing elit, sed diam nonummy nibh euismod tincidunt ut laoreet dolore magna aliquam erat aliquam lorem volutpat.</p>
  </div>
  <div class="work abs" role="img" aria-label="Photograph of a businessman in a suit in an office" style="left:769px;top:215px;width:291px;height:250px;background:linear-gradient(150deg,#e9eef4,#bcc8d8 55%,#3e5a86)"><span>Lorem ipsum dolor sit amet</span></div>
  <div class="work abs" role="img" aria-label="Photograph of oil pumps silhouetted at sunset" style="left:769px;top:484px;width:291px;height:245px;background:linear-gradient(180deg,#3b3a58,#d88a2a 55%,#f5c04a 70%,#1a1208)"><span>Lorem ipsum dolor sit amet</span></div>
</section>

<section class="consult">
  <h2 class="abs">Request a Free Consultation</h2>
  <p class="lead abs">Lorem ipsum dolor sit amet, consectetuer adipiscing elit, sed diam nonummy nibh euismod tincidunt ut laoreet dolore magna aliquam erat volutpat.</p>
  <div class="field abs" style="left:140px;top:195px;width:272px;height:43px">First Name</div>
  <div class="field abs" style="left:424px;top:195px;width:271px;height:43px">Phone</div>
  <div class="field abs" style="left:140px;top:257px;width:272px;height:43px">Email</div>
  <div class="field abs" style="left:424px;top:257px;width:271px;height:43px;display:flex;justify-content:space-between">Inquiry For<svg width="12" height="12" viewBox="0 0 12 12"><path d="M2 4 L6 8 L10 4" fill="none" stroke="#777" stroke-width="1.5"/></svg></div>
  <div class="field abs" style="left:140px;top:316px;width:555px;height:79px">Message</div>
  <span class="btn abs">Submit Now</span>
  <div class="consult-photo abs" role="img" aria-label="Photograph of business people reviewing charts on a tablet"></div>
</section>

<section class="contact">
  <div class="contact-col abs" style="left:0;width:507px;padding-left:120px">
    <div class="icon"><svg width="18" height="24" viewBox="0 0 18 24"><path d="M9 1 C4 1 1 5 1 9 C1 15 9 23 9 23 C9 23 17 15 17 9 C17 5 14 1 9 1Z" fill="none" stroke="#fff" stroke-width="2"/><circle cx="9" cy="9" r="3" fill="#fff"/></svg></div>
    12 Lorem ipsum dolor 456 Sed diam nonuy
  </div>
  <div class="divider abs" style="left:507px"></div>
  <div class="contact-col abs" style="left:507px;width:267px">
    <div class="icon"><svg width="22" height="22" viewBox="0 0 24 24"><path d="M5 2 L9 2 L11 7 L8.5 9 C10 12 12 14 15 15.5 L17 13 L22 15 L22 19 C22 21 20 22 18 22 C9 21 3 15 2 6 C2 4 3 2 5 2Z" fill="#fff"/></svg></div>
    Phone : 123-456-7890
  </div>
  <div class="divider abs" style="left:774px"></div>
  <div class="contact-col abs" style="left:774px;width:310px">
    <div class="icon"><svg width="22" height="18" viewBox="0 0 22 18" fill="none" stroke="#fff" stroke-width="2"><rect x="1" y="1" width="20" height="16"/><path d="M1 1 L11 10 L21 1"/></svg></div>
    info@marendoadvisers.com
  </div>
</section>

<footer class="footer">
  <ul class="foot-links abs"><li>Home</li><li>About Us</li><li>Services</li><li>Portfolio</li><li>Contact Us</li></ul>
  <p class="copy abs">Copyright © 2018 Marendo Advisers. All Right Reserved.</p>
  <div class="foot-brand abs">MAL</div>
  <div class="social abs"><span></span><span></span><span></span><span></span></div>
</footer>

</body>
</html>
```